PSD website for property company

Please read the brief thoroughly.

We are looking for a new website for a property group that does property acquisitions, property development and property management.
They buy, build and lease core inner city industrial assets in Sydney, Australia.
They also invest in residential developments.

Site menu
- Home page
- Property – sub menus include – Leasing ; Projects ; Investments ; Property Management
- Capital and finance
- About
- Contact

They like this website
https://www.verlo.com.au/

They want the site to be clean, modern and bold.
They like few colors, even black and white is OK to submit

They have a logo and style guide and useable images here:
http://www.kumet.net/temp/PelorisWeb2019.zip
The zip file is also attached to this project.
We have supplied some images to give you an idea, but we will also require you to provide at least 3 extra images from stock photos.
Use your imagination.

I am expecting a lot of similar designs, so be aware the photos you choose will be really important.
They want really 3 good stock photos used and supplied without charge.
Please not too generic, I repeat the quality of the photos is important.
You may provide several photos (but not in multiple submissions please) and we will choose the best three to be provided.

The winner will be selected on a single home page design and required to provide;
All photos use in original format without charge
A second ‘standard page’ template design based on the winning home page design

```html
<!DOCTYPE html>
<html lang="en">
<head>
<meta charset="utf-8">
<title>Peloris Property Groups</title>
<link rel="stylesheet" href="https://fonts.googleapis.com/css2?family=Poppins:wght@300;400;500;600;700&family=Roboto:wght@500;700&display=swap">
<style>
:root{
  --ink:#000;
  --text:#222;
  --muted:#8a8a8a;
  --paper:#fff;
  --soft:#f7f7f7;
  --band:#ededed;
  --line:#222;
}
*{box-sizing:border-box;margin:0;padding:0}
html,body{width:1200px;height:3229px;overflow:hidden}
body{position:relative;background:var(--paper);font-family:"Poppins",sans-serif;color:var(--text)}
.abs{position:absolute}
h1,h2,h3{line-height:1.2}
.heading{font-family:"Roboto",sans-serif;font-weight:700;color:var(--text)}

/* header */
.site-header{left:0;top:0;width:1200px;height:75px;background:var(--paper)}
.brand{left:29px;top:22px;font-family:"Poppins",sans-serif;font-weight:600;font-size:30px;letter-spacing:7px;color:var(--ink);line-height:30px}
.nav a{position:absolute;top:28px;font-size:13px;color:#333;text-decoration:none;white-space:nowrap}
.search{left:1140px;top:26px}

/* hero */
.hero{left:0;top:75px;width:1200px;height:480px;background:linear-gradient(180deg,#b9c8d6 0%,#c8c4bd 45%,#8f8f78 78%,#6e7a4c 100%)}
.hero-title{left:0;top:107px;width:1200px;text-align:center;font-family:"Poppins",sans-serif;font-weight:600;font-size:52px;line-height:62px;color:#fff;letter-spacing:1px}
.btn-dark{background:var(--ink);color:#fff;font-size:13px;display:flex;align-items:center;justify-content:center}
.contact-rail{left:1169px;top:185px;width:31px;height:111px;background:var(--ink)}
.slider-bar{left:0;top:397px;width:1073px;height:83px;background:rgba(235,235,235,.72)}
.slider-count{top:30px;font-size:19px;line-height:22px;font-weight:600;color:#111}
.slider-caption{left:735px;top:34px;font-size:12px;line-height:16px;color:#9a9a9a;white-space:nowrap}

/* about */
.about{left:0;top:555px;width:1200px;height:574px;background:var(--soft)}
.about-block{left:0;top:75px;width:497px;height:339px;background:var(--ink)}
.about-photo{left:34px;top:110px;width:549px;height:391px;background:linear-gradient(160deg,#6d9fca 0%,#3c6f9e 45%,#a7b7c6 100%)}
.about-title{left:685px;top:175px;font-size:35px;letter-spacing:1px}
.about-rule{left:621px;top:249px;width:52px;height:1px;background:#444}
.about-text{left:685px;top:240px;width:376px;font-size:12.5px;line-height:19px;color:var(--muted);letter-spacing:.3px}
.about-btn{left:685px;top:367px;width:131px;height:34px}
.social-rail{left:1121px;top:191px;width:43px;height:152px;background:#aaa}

/* services */
.section-title{left:0;width:1200px;text-align:center;font-size:35px;letter-spacing:1px}
.service-band{background:var(--band)}
.card{width:485px;height:301px;background:var(--ink)}
.card-photo{left:0;top:0;width:243px;height:301px}
.card-title{left:263px;top:47px;font-family:"Poppins",sans-serif;font-weight:600;font-size:18px;color:#fff}
.card-text{left:263px;top:91px;width:210px;font-size:13px;line-height:19px;color:#fff}
.card-btn{left:267px;top:217px;width:117px;height:38px;border:1px solid #fff;color:#fff;font-size:12px;display:flex;align-items:center;justify-content:center}

/* projects */
.projects-band{left:601px;top:2014px;width:599px;height:308px;background:var(--band)}
.projects-sub{left:300px;top:2124px;width:600px;text-align:center;font-size:13px;line-height:19px;color:var(--muted)}
.pager{width:26px;height:25px;border:1px solid #333;background:#fff;display:flex;align-items:center;justify-content:center}

/* queries */
.queries{left:0;top:2597px;width:1200px;height:569px;background:linear-gradient(90deg,#2b2730 0%,#3d3340 45%,#5c4a3c 75%,#2e2a30 100%)}
.query-card{left:172px;top:2622px;width:493px;height:519px;background:#fff}
.query-title{left:21px;top:42px;font-size:33px}
.query-rule{left:25px;top:90px;width:108px;height:1px;background:#333}
.tab{position:absolute;top:136px;font-size:12.5px;color:#333;white-space:nowrap}
.tab-active{left:26px;top:159px;width:46px;height:2px;background:#333}
.field-label{position:absolute;left:48px;font-size:12.5px;color:#333}
.field-line{position:absolute;left:41px;width:410px;height:1px;background:#333}
.submit{left:41px;top:419px;width:410px;height:40px;background:var(--ink);color:#fff;font-size:15px;display:flex;align-items:center;justify-content:center}

/* footer */
.site-footer{left:0;top:3166px;width:1200px;height:63px;background:var(--ink);color:#fff;font-size:12px}
</style>
</head>
<body>

<header class="abs site-header">
  <div class="abs brand">PELORIS</div>
  <nav class="nav">
    <a style="left:416px">Home</a>
    <a style="left:484px">Property &#8964;</a>
    <a style="left:581px">Capital &amp; Finance</a>
    <a style="left:724px">About</a>
    <a style="left:793px">Contact</a>
    <a style="left:1001px">Log In / Sign Up</a>
  </nav>
  <svg class="abs search" width="24" height="24" viewBox="0 0 24 24" fill="none" stroke="#222" stroke-width="1.6"><circle cx="10" cy="10" r="8"/><line x1="16" y1="16" x2="22" y2="22"/></svg>
</header>

<section class="abs hero" role="img" aria-label="Courtyard of a modern arched commercial building with people on the lawn">
  <h1 class="abs hero-title">Peloris Property Groups</h1>
  <div class="abs btn-dark" style="left:513px;top:212px;width:174px;height:43px">Explore Our Projects</div>
  <div class="abs contact-rail">
    <svg class="abs" style="left:8px;top:12px" width="14" height="14" viewBox="0 0 24 24" fill="#fff"><path d="M6 2l4 5-2 3c1 3 3 5 6 6l3-2 5 4-3 4C10 22 2 14 2 5z"/></svg>
    <svg class="abs" style="left:9px;top:45px" width="12" height="16" viewBox="0 0 12 16" fill="#fff"><path d="M6 0a6 6 0 0 1 6 6c0 4-6 10-6 10S0 10 0 6a6 6 0 0 1 6-6z"/><circle cx="6" cy="6" r="2" fill="#000"/></svg>
    <svg class="abs" style="left:7px;top:82px" width="17" height="12" viewBox="0 0 17 12"><rect width="17" height="12" fill="#fff"/><path d="M0 0l8.5 7L17 0" stroke="#000" fill="none"/></svg>
  </div>
  <div class="abs slider-bar">
    <svg class="abs" style="left:125px;top:36px" width="48" height="12" viewBox="0 0 48 12" fill="none" stroke="#333"><path d="M47 6H2M7 1L2 6l5 5"/></svg>
    <svg class="abs" style="left:216px;top:36px" width="48" height="12" viewBox="0 0 48 12" fill="none" stroke="#333"><path d="M1 6h45M41 1l5 5-5 5"/></svg>
    <span class="abs slider-count" style="left:451px">01</span>
    <div class="abs" style="left:480px;top:42px;width:38px;height:2px;background:#111"></div>
    <div class="abs" style="left:518px;top:42px;width:50px;height:1px;background:#aaa"></div>
    <span class="abs" style="left:577px;top:35px;font-size:12px;line-height:16px;color:#888">03</span>
    <div class="abs" style="left:680px;top:42px;width:47px;height:1px;background:#888"></div>
    <span class="abs slider-caption">85 Nemo enim ipsam voluptatem quia voluptas</span>
  </div>
</section>

<section class="abs about">
  <div class="abs about-block"></div>
  <div class="abs about-photo" role="img" aria-label="Glass office towers seen from below against a blue sky"></div>
  <h2 class="abs heading about-title">About Peloris</h2>
  <div class="abs about-rule"></div>
  <p class="abs about-text">We are a property group. We do property acquisitions, property development and property management.<br>We buy, build and lease core inner city industrial assets in Sydney, Australia. We also invest in residential developments.</p>
  <div class="abs btn-dark about-btn">Read More</div>
  <div class="abs social-rail">
    <svg class="abs" style="left:15px;top:22px" width="12" height="114" viewBox="0 0 12 114" fill="#fff">
      <circle cx="6" cy="6" r="5"/><circle cx="6" cy="36" r="5"/><circle cx="6" cy="66" r="5"/><rect x="1" y="91" width="10" height="10"/>
    </svg>
  </div>
</section>

<h2 class="abs heading section-title" style="top:1183px">Our Services</h2>
<div class="abs service-band" style="left:0;top:1299px;width:1200px;height:339px"></div>
<div class="abs service-band" style="left:0;top:1638px;width:449px;height:113px"></div>
<div class="abs service-band" style="left:760px;top:1638px;width:440px;height:113px"></div>

<article class="abs card" style="left:104px;top:1294px">
  <div class="abs card-photo" style="background:linear-gradient(180deg,#8fb4d8 0%,#4a4f5a 55%,#2c2a24 100%)" role="img" aria-label="Lit apartment tower at dusk"></div>
  <h3 class="abs card-title">Property Leasing</h3>
  <p class="abs card-text">Itaque earum rerum hic tenetur a sapiente delectus, ut aut reiciendis voluptatibus maiores alias consequatur aut perferendis</p>
  <div class="abs card-btn">Read More</div>
</article>
<article class="abs card" style="left:611px;top:1294px">
  <div class="abs card-photo" style="background:linear-gradient(180deg,#e9ebec 0%,#c9c9c4 55%,#8d8d88 100%)" role="img" aria-label="Bright open-plan apartment living room"></div>
  <h3 class="abs card-title">Property Investment</h3>
  <p class="abs card-text">Itaque earum rerum hic tenetur a sapiente delectus, ut aut reiciendis voluptatibus maiores alias consequatur aut perferendis</p>
  <div class="abs card-btn">Read More</div>
</article>
<article class="abs card" style="left:104px;top:1638px">
  <div class="abs card-photo" style="background:linear-gradient(180deg,#c9d6e4 0%,#b7b8b2 55%,#4f6a3c 100%)" role="img" aria-label="Row of painted terrace houses"></div>
  <h3 class="abs card-title">Property Management</h3>
  <p class="abs card-text">Itaque earum rerum hic tenetur a sapiente delectus, ut aut reiciendis voluptatibus maiores alias consequatur aut perferendis</p>
  <div class="abs card-btn">Read More</div>
</article>
<article class="abs card" style="left:611px;top:1638px">
  <div class="abs card-photo" style="background:linear-gradient(180deg,#6b5040 0%,#c9d2d6 35%,#7a8a5c 65%,#8a6a4c 100%)" role="img" aria-label="Rooftop terrace with outdoor seating"></div>
  <h3 class="abs card-title">Capital &amp; Finance</h3>
  <p class="abs card-text">Itaque earum rerum hic tenetur a sapiente delectus, ut aut reiciendis voluptatibus maiores alias consequatur aut perferendis</p>
  <div class="abs card-btn">Read More</div>
</article>

<div class="abs projects-band"></div>
<h2 class="abs heading section-title" style="top:2078px">Our Projects</h2>
<p class="abs projects-sub">Quis autem vel eum iure reprehenderit qui in ea voluptate velit esse quam nihil molestiae consequatur, vel illum qui dolorem eum fugiat</p>
<div class="abs" style="left:192px;top:2228px;width:257px;height:225px;background:linear-gradient(180deg,#9fb2c0 0%,#c9a27a 55%,#7a5a3a 100%)" role="img" aria-label="Shopping mall interior"></div>
<div class="abs" style="left:449px;top:2208px;width:302px;height:265px;background:linear-gradient(180deg,#7fa9d9 0%,#5a7088 50%,#6d8a58 100%)" role="img" aria-label="Glass office building with trees"></div>
<div class="abs" style="left:751px;top:2228px;width:258px;height:225px;background:linear-gradient(180deg,#a7c2d4 0%,#c97a38 50%,#2c2420 100%)" role="img" aria-label="Office lounge with yellow chairs"></div>
<div class="abs pager" style="left:568px;top:2503px"><svg width="8" height="10" viewBox="0 0 8 10" fill="none" stroke="#333"><path d="M6 1L2 5l4 4"/></svg></div>
<div class="abs pager" style="left:606px;top:2503px"><svg width="8" height="10" viewBox="0 0 8 10" fill="none" stroke="#333"><path d="M2 1l4 4-4 4"/></svg></div>

<section class="abs queries" role="img" aria-label="Residential villa with pool at dusk"></section>
<form class="abs query-card">
  <h2 class="abs heading query-title">Your Queries</h2>
  <div class="abs query-rule"></div>
  <span class="tab" style="left:26px">Leasing</span>
  <span class="tab" style="left:110px">Development</span>
  <span class="tab" style="left:231px">Management</span>
  <span class="tab" style="left:352px">Capital &amp; Finance</span>
  <div class="abs tab-active"></div>
  <span class="field-label" style="top:194px">Your Name*</span>
  <div class="field-line" style="top:225px"></div>
  <span class="field-label" style="top:234px">Your Email*</span>
  <div class="field-line" style="top:264px"></div>
  <span class="field-label" style="top:272px">Message*</span>
  <div class="field-line" style="top:401px"></div>
  <div class="abs submit">Submit</div>
</form>

<footer class="abs site-footer">
  <span class="abs" style="left:172px;top:24px">©Copyright information here</span>
  <span class="abs" style="left:717px;top:24px">Terms &amp; Conditions | Privacy Policy | Contact Us</span>
</footer>

</body>
</html>
```